House-share and Room Rental Website (With Focus on the Bedroom Landing Page)

Looking for website design for our House-share (executive accommodation) and room rental business.

Our company name is: Lodvenra could also be written as LodVenra or lodvenra. Either is fine .. just looking for a nice clean catchy logo to go with the design.

EXAMPLES
These are examples of other websites in this field that are doing well. this is a kind of baseline.
https://kelbrin.com.au/
https://www.tuvaplex.com/
https://www.nestorvi.com/
https://www.quillsa.net/
https://www.pendlebarrow.com.au/

Our business model is to rent rooms to people looking for high-quality accommodation. We fill the gap between those looking to rent rooms and those with rooms to rent. However, our model is slightly different from those already on the market as we looking to fill a massive gap in the market delivering upmarket rooms for rent.(Executive Accommodation) also in the back end will be coupled with a self management process in the back end.

We offer executive style accommodation that stands out above the rest. With special extras like fire safety.. and management processes that create happier homes. We are looking for a web design package that can help us grow and scale our business. We need a design that is captivating

Our MAIN focus is having a room landing page that stands out from the rest... The core of our business will rely on the promotion of the rooms in a share house... so the whole design relies on the BEDROOM landing page to drive results.

Target Market(s)

We have 2 markets we are aiming at ... the first market is people offering rooms to rent who want the highest rental return. The second market is people looking to rent safe, high-quality rooms, in houses that are well managed and looked after.

Industry/Entity Type

Share Economy

Logo Text

LodVenra

Number of Pages Required

5+ page

Font styles to use
Sans Serif

Colors
3276b5

Requirements
Must have
• A messaging system whereby we can create direct communication between those offering rooms and those looking for rooms.
• A call to action that says " Schedule an Inspection"
• Landing page for promoting rooms
• A home page for showing stock.
• Profile page for those selling rooms
• Profile page for those looking for rooms.
• A scheduling calendar for booking inspections
Nice to have
• Pages where new residents can lock in a room.. pay bond and rents.. and sign contracts
• Notifications
• SMS capabilities in the backend.
Should not have
• No script or handwriting fonts.

```html
<!DOCTYPE html>
<html lang="en">
<head>
<meta charset="utf-8">
<title>Lodvenra – Executive Accommodation for Two</title>
<link rel="stylesheet" href="https://fonts.googleapis.com/css2?family=Questrial&family=Open+Sans:wght@600&display=swap">
<style>
  :root {
    --brand: #3276b5;
    --brand-deep: #0f4e9c;
    --brand-mid: #2d6db3;
    --navy: #1b2a6b;
    --footer-base: #173e6e;
    --rule: #c9c9c9;
    --white: #ffffff;
    --ink-soft: #555a66;
  }
  * { box-sizing: border-box; margin: 0; padding: 0; }
  html, body { width: 714px; height: 1200px; overflow: hidden; background: var(--white); }
  body { position: relative; font-family: "Questrial", sans-serif; color: var(--brand); }

  .site-header { position: absolute; left: 0; top: 0; width: 714px; height: 72px; background: var(--white); }
  .brand-name { position: absolute; left: 18px; top: 15px; font-size: 29px; color: var(--brand); letter-spacing: 0.2px; }
  .header-rule { position: absolute; left: 0; top: 72px; width: 714px; height: 5px; background: var(--brand); }

  .hero { position: absolute; left: 0; top: 77px; width: 714px; height: 403px; overflow: hidden; }
  .hero-photo { position: absolute; inset: 0;
    background:
      radial-gradient(ellipse 260px 120px at 300px 300px, rgba(120,120,125,0.55), transparent 70%),
      linear-gradient(120deg, #5a5a5c 0%, #3a3a3c 35%, #2a2a2c 60%, #1e1e20 100%); }
  .hero-title { position: absolute; left: 0; width: 714px; top: 102px; text-align: center; color: var(--white);
    font-weight: 400; font-size: 24px; letter-spacing: 0.2px; }
  .hero-copy { position: absolute; left: 177px; width: 350px; top: 150px; text-align: center; color: var(--white);
    font-family: "Open Sans", sans-serif; font-weight: 600; font-size: 10px; line-height: 22.4px; }
  .hero-cta { position: absolute; left: 235px; top: 242px; width: 205px; height: 36px; border-radius: 5px;
    background: var(--brand); color: var(--white); font-size: 15px; text-align: center; line-height: 36px; }
  .hero-arrow { position: absolute; top: 144px; }
  .hero-arrow.prev { left: 18px; }
  .hero-arrow.next { left: 658px; }

  .room-facts { position: absolute; left: 0; top: 480px; width: 714px; height: 47px; background: var(--brand-deep); }
  .fact { position: absolute; top: 0; height: 47px; color: var(--white); }
  .fact.alt { background: var(--brand-mid); }
  .fact svg { position: absolute; top: 9px; }
  .fact-label { position: absolute; top: 11px; font-size: 9px; letter-spacing: -0.1px; white-space: nowrap; }
  .fact-value { position: absolute; top: 26px; font-size: 12px; white-space: nowrap; }

  .info-card { position: absolute; top: 559px; width: 243px; height: 206px; border: 2px solid var(--rule); background: var(--white); }
  .info-card.room { left: 94px; }
  .info-card.public { left: 381px; }
  .card-heading { position: absolute; font-size: 12px; font-weight: 400; color: var(--navy); letter-spacing: 0.2px; }
  .amenity-list { position: absolute; list-style: none; }
  .amenity-list li { position: relative; height: 22.4px; font-size: 12px; color: var(--brand); padding-left: 23px; white-space: nowrap; }
  .amenity-list li svg { position: absolute; left: 0; top: 3px; }
  .core-row { position: absolute; left: 28px; font-size: 10.5px; white-space: nowrap; }
  .core-row .key { color: var(--brand); display: inline-block; width: 52px; }
  .core-row .val { color: var(--ink-soft); }

  .site-footer { position: absolute; left: 0; top: 980px; width: 714px; height: 220px; background: var(--brand); border-top: 3px solid var(--brand-deep); }
  .footer-col h3 { font-weight: 400; font-size: 15.5px; color: var(--white); margin-bottom: 8px; letter-spacing: 0.2px; }
  .footer-col p { font-size: 12px; color: var(--white); line-height: 17.6px; }
  .footer-col.contact { position: absolute; left: 12px; top: 80px; }
  .footer-col.links { position: absolute; left: 593px; top: 80px; }
  .footer-brand { position: absolute; left: 196px; top: 84px; width: 320px; text-align: center; font-size: 50px; color: var(--white); }
  .footer-base { position: absolute; left: 0; bottom: 0; width: 714px; height: 20px; background: var(--footer-base);
    color: var(--white); font-size: 9px; line-height: 20px; }
  .footer-base .copy { position: absolute; left: 12px; }
  .footer-base .legal { position: absolute; right: 10px; }

  .location-map { position: absolute; left: 228px; top: 794px; width: 270px; height: 240px; border: 4px solid var(--brand);
    background: linear-gradient(135deg, #e8e4dc 0%, #dedad0 50%, #e6e2d8 100%); }
</style>
</head>
<body>
  <header class="site-header">
    <div class="brand-name">lodvenra</div>
  </header>
  <div class="header-rule"></div>

  <section class="hero">
    <div class="hero-photo" role="img" aria-label="Dimly lit executive bedroom with a double bed against a concrete wall"></div>
    <h1 class="hero-title">EXCEUTIVE ACCOMODATION FOR TWO</h1>
    <p class="hero-copy">Lorem ipsum dolor sit amet, consectetur adipiscing elit, sed do eiusmod tempor incididunt ut labore et dolore magna aliqua. Ut enim ad minim veniam, quis nostrud exercitation commodo consequat</p>
    <div class="hero-cta">Schedule an Inspection</div>
    <svg class="hero-arrow prev" width="38" height="52" viewBox="0 0 38 52"><polyline points="36,2 2,26 36,50" fill="none" stroke="#ffffff" stroke-width="2"/></svg>
    <svg class="hero-arrow next" width="38" height="52" viewBox="0 0 38 52"><polyline points="2,2 36,26 2,50" fill="none" stroke="#3276b5" stroke-width="2.5"/></svg>
  </section>

  <section class="room-facts">
    <div class="fact" style="left:0;width:136px">
      <svg style="left:10px" width="32" height="28" viewBox="0 0 32 28" fill="none" stroke="#fff" stroke-width="2"><path d="M3 4v18h26"/><path d="M1 24h30"/><circle cx="20" cy="11" r="8"/><path d="M20 11l4-4"/></svg>
      <div class="fact-label" style="left:52px">INTERNET SPEED</div>
      <div class="fact-value" style="left:52px">2 mbps</div>
    </div>
    <div class="fact alt" style="left:136px;width:121px">
      <svg style="left:16px;top:14px" width="42" height="20" viewBox="0 0 42 20" fill="#fff"><rect x="0" y="0" width="3" height="20"/><rect x="39" y="6" width="3" height="14"/><rect x="0" y="11" width="42" height="5"/><circle cx="8" cy="7" r="3.5"/><rect x="13" y="5" width="26" height="6" rx="2"/></svg>
      <div class="fact-label" style="left:67px">BED SIZE</div>
      <div class="fact-value" style="left:67px">6 by 6</div>
    </div>
    <div class="fact" style="left:257px;width:151px">
      <svg style="left:8px" width="28" height="30" viewBox="0 0 28 30" fill="none" stroke="#fff" stroke-width="2.2"><circle cx="10" cy="14" r="6"/><path d="M10 20v9M6 25h8"/><circle cx="16" cy="11" r="6"/><path d="M20 7l6-6M21 1h5v5"/></svg>
      <div class="fact-label" style="left:42px">GENDER PREFERENCE</div>
      <div class="fact-value" style="left:42px">Couple</div>
    </div>
    <div class="fact alt" style="left:408px;width:117px">
      <svg style="left:9px;top:7px" width="24" height="34" viewBox="0 0 24 34" fill="none" stroke="#fff" stroke-width="2"><path d="M12 26C5 17 3 14 3 10a9 9 0 0118 0c0 4-2 7-9 16z"/><circle cx="12" cy="10" r="3.5"/><path d="M4 28c2 3 14 3 16 0"/></svg>
      <div class="fact-label" style="left:41px">ROOM AREA</div>
      <div class="fact-value" style="left:41px">400 sqm</div>
    </div>
    <div class="fact" style="left:525px;width:189px">
      <svg style="left:9px;top:8px" width="30" height="32" viewBox="0 0 30 32" fill="#fff"><path d="M4 2h6v3H7v11H4z"/><rect x="1" y="15" width="28" height="3"/><path d="M3 18h24l-2 9H5z"/><rect x="6" y="27" width="2" height="4"/><rect x="22" y="27" width="2" height="4"/><path d="M11 5l8 0-2 4h-4z"/></svg>
      <div class="fact-label" style="left:49px">BATHROOM TYPE</div>
      <div class="fact-value" style="left:53px">Shared</div>
    </div>
  </section>

  <section class="info-card room">
    <h2 class="card-heading" style="left:52px;top:16px">ROOM AMENITIES</h2>
    <ul class="amenity-list" style="left:30px;top:38px">
      <li><svg width="10" height="10" viewBox="0 0 10 10" fill="#666"><path d="M5 0l2 2-2 2-2-2zM5 6l2 2-2 2-2-2zM0 5l2-2 2 2-2 2zM6 5l2-2 2 2-2 2z"/></svg>Furnished/unfurnished</li>
      <li><svg width="10" height="10" viewBox="0 0 10 10" fill="#666"><path d="M5 0l2 2-2 2-2-2zM5 6l2 2-2 2-2-2zM0 5l2-2 2 2-2 2zM6 5l2-2 2 2-2 2z"/></svg>TV</li>
      <li><svg width="10" height="10" viewBox="0 0 10 10" fill="#666"><path d="M5 0l2 2-2 2-2-2zM5 6l2 2-2 2-2-2zM0 5l2-2 2 2-2 2zM6 5l2-2 2 2-2 2z"/></svg>Storage space</li>
      <li><svg width="10" height="10" viewBox="0 0 10 10" fill="#666"><path d="M5 0l2 2-2 2-2-2zM5 6l2 2-2 2-2-2zM0 5l2-2 2 2-2 2zM6 5l2-2 2 2-2 2z"/></svg>Study Desk / Workstation</li>
      <li><svg width="10" height="10" viewBox="0 0 10 10" fill="#666"><path d="M5 0l2 2-2 2-2-2zM5 6l2 2-2 2-2-2zM0 5l2-2 2 2-2 2zM6 5l2-2 2 2-2 2z"/></svg>Wardrobe</li>
      <li><svg width="10" height="10" viewBox="0 0 10 10" fill="#666"><path d="M5 0l2 2-2 2-2-2zM5 6l2 2-2 2-2-2zM0 5l2-2 2 2-2 2zM6 5l2-2 2 2-2 2z"/></svg>Ensuite shower</li>
      <li><svg width="10" height="10" viewBox="0 0 10 10" fill="#666"><path d="M5 0l2 2-2 2-2-2zM5 6l2 2-2 2-2-2zM0 5l2-2 2 2-2 2zM6 5l2-2 2 2-2 2z"/></svg>Kitchenette</li>
    </ul>
  </section>

  <section class="info-card public">
    <h2 class="card-heading" style="left:32px;top:16px">PUBLIC AMMENITIES</h2>
    <ul class="amenity-list" style="left:40px;top:38px">
      <li><svg width="10" height="10" viewBox="0 0 10 10" fill="#666"><path d="M5 0l2 2-2 2-2-2zM5 6l2 2-2 2-2-2zM0 5l2-2 2 2-2 2zM6 5l2-2 2 2-2 2z"/></svg>Transport options</li>
      <li><svg width="10" height="10" viewBox="0 0 10 10" fill="#666"><path d="M5 0l2 2-2 2-2-2zM5 6l2 2-2 2-2-2zM0 5l2-2 2 2-2 2zM6 5l2-2 2 2-2 2z"/></svg>Trains</li>
      <li><svg width="10" height="10" viewBox="0 0 10 10" fill="#666"><path d="M5 0l2 2-2 2-2-2zM5 6l2 2-2 2-2-2zM0 5l2-2 2 2-2 2zM6 5l2-2 2 2-2 2z"/></svg>Busses</li>
      <li><svg width="10" height="10" viewBox="0 0 10 10" fill="#666"><path d="M5 0l2 2-2 2-2-2zM5 6l2 2-2 2-2-2zM0 5l2-2 2 2-2 2zM6 5l2-2 2 2-2 2z"/></svg>50 miles from Washington DC</li>
    </ul>
    <h2 class="card-heading" style="left:28px;top:128px">CORE INFOMATION</h2>
    <div class="core-row" style="top:155px"><span class="key">ADRESS</span><span class="val">Fenwick Street, NY Town</span></div>
    <div class="core-row" style="top:177px"><span class="key">UTILITIES</span><span class="val">Included</span></div>
  </section>

  <footer class="site-footer">
    <div class="footer-col contact">
      <h3>CONTACT US</h3>
      <p>Marlow Street 1234<br>NY, Example<br>infor@staybrell.com<br>www.staybrell.com</p>
    </div>
    <div class="footer-brand">lodvenra</div>
    <div class="footer-col links">
      <h3>QUICK LINKS</h3>
      <p>Bedrooms<br>Sitting Rooms<br>Homes</p>
    </div>
    <div class="footer-base">
      <span class="copy">© Staybrell Rooms Ltd 2019</span>
      <span class="legal">Terms | Privacy Policy</span>
    </div>
  </footer>

  <div class="location-map" role="img" aria-label="Street map showing the route from the room to nearby transport"></div>
</body>
</html>
```